PDN Letterhead

We need a letterhead design that will be able to be used on all marketing products (letterhead, mail chimp, envelops, business cards, etc.) We are a law firm specializing primarily in transportation law but offer a wide range of services to our clients. We would like the design to be modern, simple, and professional. Our colors are black and gold, however, we've incorporated dark gray and white on other marketing products such as our website.

```html
<!DOCTYPE html>
<html lang="en">
<head>
<meta charset="utf-8">
<title>PDN Law Group Letterhead</title>
<link href="https://fonts.googleapis.com/css2?family=Montserrat:wght@400;500;600&family=Mrs+Saint+Delafield&display=swap" rel="stylesheet">
<style>
  :root {
    --backdrop: #e9e9e9;
    --paper: #ffffff;
    --ink: #1b1b1b;
    --gold: #ad946a;
    --muted: #8d8d8d;
    --rule: #555555;
    --wash-grey: #ebebeb;
    --wash-cream: #f6f4ef;
  }
  * { margin: 0; padding: 0; box-sizing: border-box; }
  html, body { width: 1200px; height: 960px; overflow: hidden; }
  body {
    background: var(--backdrop);
    font-family: "Montserrat", Arial, sans-serif;
    color: var(--ink);
  }
  .letterhead {
    position: absolute;
    left: 282px; top: 30px;
    width: 636px; height: 900px;
    background: var(--paper);
    overflow: hidden;
  }
  .lower-wash {
    position: absolute; left: 0; right: 0; bottom: 0; height: 450px;
    background: linear-gradient(180deg, rgba(255,255,255,0) 0%, var(--wash-cream) 45%, var(--wash-grey) 100%);
  }
  .brand {
    position: absolute; left: 57px; top: 70px;
    display: flex; align-items: center; gap: 8px;
    font-size: 22px; font-weight: 600; letter-spacing: 2px;
    color: var(--ink);
  }
  .brand-mark { width: 14px; height: 14px; background: var(--gold); }
  .contact {
    position: absolute; left: 450px; top: 51px;
    font-size: 11px; line-height: 14px; color: var(--ink);
  }
  .contact .address { margin-bottom: 6px; }
  .contact .line { display: flex; align-items: center; gap: 7px; line-height: 14px; }
  .contact svg { width: 8px; height: 8px; flex: none; }
  .header-rule {
    position: absolute; left: 44px; top: 136px;
    width: 543px; height: 2px; background: var(--rule);
  }
  .recipient { position: absolute; left: 65px; top: 210px; }
  .recipient .label { font-size: 11px; font-weight: 500; letter-spacing: 1.5px; }
  .recipient .name { margin-top: 8px; font-size: 10.5px; font-weight: 600; color: var(--gold); }
  .recipient .details { margin-top: 6px; font-size: 8px; line-height: 14px; color: var(--muted); }
  .date {
    position: absolute; right: 68px; top: 213px;
    font-size: 8.5px; color: #555;
  }
  .body-copy {
    position: absolute; left: 65px; top: 330px; width: 504px;
    font-size: 8.7px; line-height: 11.3px; color: var(--muted);
    text-align: justify;
  }
  .body-copy p { margin-bottom: 11.3px; }
  .sign-off { position: absolute; left: 63px; top: 640px; }
  .sign-off .signature {
    font-family: "Mrs Saint Delafield", cursive;
    font-size: 32px; color: var(--ink); line-height: 34px;
  }
  .sign-off .name { margin-top: 4px; font-size: 10.5px; font-weight: 500; }
  .sign-off .title { margin-top: 2px; font-size: 8px; color: var(--muted); }
</style>
</head>
<body>
<main class="letterhead">
  <div class="lower-wash" role="img" aria-label="Soft decorative background in light cream and grey tones"></div>

  <header>
    <div class="brand"><span class="brand-mark"></span>PDN LAW GROUP</div>
    <div class="contact">
      <div class="address">Your address, city<br>state, ZIP 0000</div>
      <div class="line">
        <svg viewBox="0 0 10 10"><path d="M2 0.5 L4 2.8 L3 4 Q4.2 6 6 7 L7.2 6 L9.5 8 L8 9.6 Q3.5 9 0.4 2 Z" fill="var(--gold)"/></svg>
        123-456-2100
      </div>
      <div class="line">
        <svg viewBox="0 0 10 10"><rect x="0.5" y="2" width="9" height="6.5" fill="var(--gold)"/><path d="M0.5 2 L5 5.6 L9.5 2" stroke="#fff" stroke-width="0.9" fill="none"/></svg>
        youremail@mailbox.com
      </div>
      <div class="line">
        <svg viewBox="0 0 10 10"><circle cx="5" cy="5" r="4.3" fill="var(--gold)"/><path d="M0.7 5 H9.3 M5 0.7 Q2.6 5 5 9.3 M5 0.7 Q7.4 5 5 9.3" stroke="#fff" stroke-width="0.7" fill="none"/></svg>
        www.yourwebsite.com
      </div>
    </div>
    <div class="header-rule"></div>
  </header>

  <section class="recipient">
    <div class="label">TO</div>
    <div class="name">Daniel Harrow</div>
    <div class="details">Human Resources<br>Northwind Inc.<br>2210-B Linden Row, Fairmont<br>E42 USA</div>
  </section>
  <div class="date">Friday, 01/01/2018</div>

  <section class="body-copy">
    <p>Lorem ipsum dolor sit amet, consectetuer adipiscing elit, sed diam nonummy nibh euismod tincidunt ut laoreet dolore magna aliquam erat volutpat. Ut wisi enim ad minim veniam, quis nostrud exerci tationmcorper suscipit lobortis nisl ut aliquip ex ea commodo consequat. Duis autem vel eum iriure dolor in hendrerit in vulputate velit esse molestie consequat, vel illum dolore eu feugiat nulla facilisis at vero eros et accumsan et iusto odio dignissim qui blandit praesent luptatum zzril delenit augue duis dolore te feugait nulla facilisi.</p>
    <p>Nam liber tempor cum soluta nobis eleifend option congue nihil imprdiet doming id quod mazim placerat facer possim assum. Typi non habent claritatem insitam;</p>
    <p>Est usus legentis in iis qui facit eorum claritatem.</p>
    <p>Investigationes demonstraverunt lectores legere me lius quod ii legunt saepius. Claritas est etiam processus dynamicus, qui sequitur mutationem consuetudium lectorum. Mirum est notare quam littera gothica, quam nunc putamus parum claram, anteposuerit litterarum formas humanitatis per seacula quarta decima et quinta decima. Eodem modo typi, qui nunc nobis videntur parum clari, fiant sollemnes in futurum.</p>
    <p>consectetuer adipiscing elit, sed diam nonummy nibh euismod tincidunt ut laoreet dolore magna aliquam erat volutpat. Ut wisi enim ad minim veniam, quis nostrud exerci tation ullamcorper suscipit lobortis nisl ut aliquip ex ea commodo consequat. Duis autem vel eum iriure dolor in hendrerit in vulputate velit esse molestie consequat, vel illum dolore eu feugiat nulla facilisis at vero eros et accumsan et iusto odio dignissim qui blandit praesent luptatum zzril delenit augue duis dolore te feugait nulla facilisi.</p>
    <p>Nam liber tempor cum soluta nobis eleifend option congue nihil imperdiet .</p>
  </section>

  <footer class="sign-off">
    <div class="signature">evan marsh</div>
    <div class="name">Evan Marsh</div>
    <div class="title">Managing Director</div>
  </footer>
</main>
</body>
</html>
```